EVACUATION SIGNS FOR CABINS

ATTACHED ARE EVACUATION PLANS FOR OUR CABINS.
1. IS A BLANK EVACUTION SIGN & DIAGRAM FOR YOU TO ADD THE THREE DIFFERENT TYPES OF CABINS WE HAVE.
2. DESIGN, A EVACUTION SIGN & DIAGRAM FOR EACH CABIN STYLE.
WITH LEGEND ON EACH ONE SHOWING WHAT IS IN EACH CABIN FOR FIRE SAFETY.

```html
<!DOCTYPE html>
<html lang="en">
<head>
<meta charset="utf-8">
<title>Evacuation Sign &amp; Diagram</title>
<link href="https://fonts.googleapis.com/css2?family=Arimo:wght@400;700&family=Tinos:wght@400;700&display=swap" rel="stylesheet">
<style>
:root{
  --frame-blue:#1a1ad6;
  --alert-red:#e8141c;
  --safe-green:#19a84a;
  --ink:#111;
  --paper:#fff;
}
*{box-sizing:border-box;margin:0;padding:0}
html,body{width:844px;height:1200px;overflow:hidden;background:var(--paper)}
body{font-family:"Arimo",Arial,sans-serif;color:var(--ink);position:relative}
.sign-frame{position:absolute;left:18px;top:15px;width:808px;height:1166px;border:3px solid var(--frame-blue)}
.abs{position:absolute}
.sign-title{left:0;width:844px;top:68px;text-align:center;color:var(--alert-red);font-weight:700;font-size:26px;letter-spacing:.5px}
.sign-sub{left:0;width:844px;text-align:center;font-weight:700;font-size:13px}
.unit-label{left:360px;top:172px;font-weight:700;font-size:21px}
.legend{left:24px;top:252px;width:144px;height:161px;border:1px solid var(--ink);font-family:"Tinos",serif;font-size:13px;padding:6px 6px}
.legend-row{position:absolute;left:6px}
.floor-plan{left:212px;top:200px;width:426px;height:407px;background:linear-gradient(#e2e2e2,#cfcfcf)}
.box{position:absolute;border:2px solid var(--ink)}
.box-head{color:var(--alert-red);font-weight:700;text-align:center;font-size:14px;margin-top:6px}
.procedures{left:24px;top:694px;width:510px;height:156px;padding:4px 8px;font-size:8px;line-height:1.25}
.stage{color:var(--alert-red);font-weight:700;font-size:9.5px;margin-top:3px}
.stage span{color:var(--safe-green)}
.safety{left:542px;top:694px;width:267px;height:156px;padding:4px 8px;font-size:10px}
.safety .box-head{color:var(--frame-blue)}
.safety ul{list-style:none;margin-top:4px}
.safety li{padding-left:14px;position:relative;line-height:1.2}
.safety li::before{content:"";position:absolute;left:0;top:3px;width:7px;height:7px;border:1px solid var(--ink)}
.warn{color:var(--alert-red);font-weight:700}
.mobility{position:absolute;left:8px;top:78px;width:160px;height:68px;border:1px solid var(--ink);font-family:"Tinos",serif;font-weight:700;font-size:10px;padding:4px 6px;line-height:1.2}
.access{position:absolute;left:180px;top:78px;width:72px;height:68px;border:1px solid var(--ink);display:flex;align-items:center;justify-content:center}
.extinguisher-op{left:24px;top:859px;width:337px;height:146px;padding:2px 10px;font-size:9px;overflow:hidden}
.extinguisher-op .box-head{margin-top:4px}
.extinguisher-op ul{list-style:none;margin:6px 0 0 12px;line-height:1.2}
.extinguisher-op li::before{content:"\27A4  ";}
.extinguisher-op .pass{margin-left:22px}
.extinguisher-op .pass::before{content:"\25A1  "}
.extinguisher-op .closing{margin-top:3px;font-size:8.5px;white-space:nowrap}
.equipment{left:24px;top:1013px;width:337px;height:145px;padding:4px 10px;font-size:10px;text-align:center}
.equipment .kind{font-weight:700;font-size:12.5px;margin-top:10px}
.key-table{left:370px;top:859px;width:180px;height:299px;padding:8px 6px}
.key-row{position:absolute;left:6px;height:20px;display:flex;align-items:center;width:168px}
.key-row .icon{width:28px;height:20px;display:flex;align-items:center;justify-content:center}
.key-row .name{margin-left:8px;border:1px solid var(--ink);font-size:8px;padding:3px 4px;flex:1}
.race{left:556px;top:859px;width:253px;height:299px}
.race-inner{position:absolute;left:8px;top:14px;width:222px;height:66px;border:2px solid var(--alert-red);padding:6px 8px;font-family:"Tinos",serif;color:var(--alert-red)}
.race-inner .big{font-size:21px;font-weight:700;letter-spacing:-.5px;white-space:nowrap}
.race-inner .small{font-size:9px;font-weight:700;text-decoration:underline;margin-top:4px}
.race-step{position:absolute;left:8px;font-family:"Tinos",serif;color:var(--alert-red);font-size:14px;letter-spacing:-.3px;white-space:nowrap;line-height:1}
.race-step b{font-size:30px;font-weight:400;line-height:1}
.race-note{position:absolute;left:30px;font-family:"Tinos",serif;font-size:6.5px;font-weight:700;white-space:nowrap}
.race-note em{color:var(--safe-green);font-style:normal}
</style>
</head>
<body>
<div class="sign-frame"></div>

<h1 class="abs sign-title">EVACUATION SIGN &amp; DIAGRAM</h1>
<p class="abs sign-sub" style="top:102px">SEABREEZE HOLIDAY PARK</p>
<p class="abs sign-sub" style="top:119px">212 COASTAL DRIVE, MARLOW BAY, QLD. 4700</p>
<p class="abs unit-label">UNIT</p>

<div class="abs legend">
  <div class="legend-row" style="top:6px">LEGEND</div>
  <div class="legend-row" style="top:45px">Exit Sign -</div>
  <svg class="abs" style="left:78px;top:30px" width="44" height="20"><rect width="44" height="20" fill="var(--safe-green)"/><text x="22" y="13" font-size="6" fill="#fff" text-anchor="middle" font-family="Arimo,sans-serif">EXIT</text></svg>
  <div class="legend-row" style="top:80px">Exit Path -</div>
  <svg class="abs" style="left:78px;top:68px" width="56" height="14"><rect x="0" y="5" width="44" height="4" fill="var(--alert-red)"/><polygon points="42,0 56,7 42,14" fill="var(--alert-red)"/></svg>
  <div class="legend-row" style="top:110px">Fire Blanket –</div>
  <svg class="abs" style="left:92px;top:100px" width="14" height="24"><rect width="14" height="24" rx="4" fill="var(--alert-red)"/></svg>
  <div class="legend-row" style="top:138px">Fire Alarms -</div>
  <svg class="abs" style="left:88px;top:134px" width="22" height="14"><ellipse cx="11" cy="5" rx="10" ry="4" fill="#fff" stroke="#111"/><path d="M1 5v4a10 4 0 0 0 20 0V5" fill="#fff" stroke="#111"/></svg>
</div>

<div class="abs floor-plan" role="img" aria-label="Floor plan of the cabin unit showing carport, bedrooms with single and queen beds, kitchen, bathroom, living area and deck"></div>
<svg class="abs" style="left:505px;top:420px" width="30" height="82"><rect x="11" y="0" width="8" height="58" fill="var(--alert-red)"/><polygon points="0,56 30,56 15,82" fill="var(--alert-red)"/></svg>
<svg class="abs" style="left:494px;top:508px" width="52" height="18"><rect width="52" height="18" fill="var(--safe-green)"/><text x="26" y="12" font-size="6" fill="#fff" text-anchor="middle" font-family="Arimo,sans-serif">EXIT</text></svg>

<svg class="abs" style="left:30px;top:648px" width="680" height="40" aria-label="Safety symbol strip">
  <g fill="var(--alert-red)"><rect x="6" y="10" width="12" height="28" rx="4"/><rect x="26" y="8" width="12" height="30" rx="4"/><rect x="46" y="6" width="12" height="32" rx="4"/></g>
  <rect x="232" y="12" width="40" height="22" fill="var(--safe-green)"/><text x="252" y="26" font-size="7" fill="#fff" text-anchor="middle">AA</text>
  <rect x="300" y="20" width="40" height="4" fill="var(--safe-green)"/>
  <polygon points="354,16 372,16 372,9 388,22 372,35 372,28 354,28" fill="#fff" stroke="var(--safe-green)" stroke-width="2"/>
  <rect x="400" y="10" width="32" height="26" fill="#111"/><polygon points="420,12 408,25 417,25 412,34 426,20 417,20" fill="#f5c400"/>
  <rect x="444" y="8" width="32" height="28" fill="var(--safe-green)"/><path d="M456 12h8v8h8v8h-24v-8h8z" fill="#fff"/>
  <rect x="486" y="10" width="30" height="24" fill="var(--alert-red)"/><text x="501" y="27" font-size="13" font-weight="700" fill="#fff" text-anchor="middle">FB</text>
  <circle cx="538" cy="22" r="11" fill="#fff" stroke="var(--alert-red)" stroke-width="4"/>
  <rect x="562" y="8" width="36" height="28" fill="var(--safe-green)"/><text x="580" y="27" font-size="12" font-weight="700" fill="#fff" text-anchor="middle">EXIT</text>
  <rect x="612" y="8" width="24" height="28" fill="var(--alert-red)"/>
  <rect x="648" y="10" width="26" height="26" fill="var(--alert-red)"/><rect x="655" y="17" width="12" height="12" fill="#fff"/>
</svg>

<section class="box procedures">
  <h2 class="box-head">EVACUATION PROCEDURES</h2>
  <p class="stage">STAGE 1:- Removal of people from the immediate Danger Area</p>
  <p>Occupants and staff in the immediate danger area are to move a safe distance away from the fire and smoke. When the area has been cleared, all doors and windows should be closed to contain the fire.</p>
  <p class="stage">STAGE 2:- Removal to a Safe Area</p>
  <p>If the severity of the smoke or fire warrants further evacuation, occupants should pass through fire or smoke doors to a safe area.</p>
  <p class="stage">STAGE 3:- Complete Evacuation of Entire Complex</p>
  <p>Should the situation continue to worsen, all occupants are to leave the complex by the nearest exit and move to the assembly area.</p>
  <p class="stage">STAGE 4:- Roll Call.</p>
  <p>To be conducted as soon as possible and to ensure all Persons are accounted for. Report all missing persons to <span class="warn">FIRE OFFICERS.</span></p>
  <p class="stage">STAGE 6:- <span>ASSEMBLY AREA</span></p>
</section>

<section class="box safety">
  <h2 class="box-head">SAFETY MEASURES</h2>
  <ul>
    <li>Always turn off all electrical appliances and shut all doors.</li>
    <li>Your first role is life safety. Only attempt to extinguish fire <span class="warn">IF SAFE TO DO SO.</span></li>
  </ul>
  <p class="mobility">Mobility impaired persons should evacuate immediately on hearing the fire alarm assisted by a nominated person.</p>
  <div class="access"><svg width="48" height="48" viewBox="0 0 48 48"><rect width="48" height="48" fill="#111"/><circle cx="22" cy="9" r="4" fill="#fff"/><path d="M20 15v14h12l5 11" fill="none" stroke="#fff" stroke-width="4"/><path d="M16 22a10 10 0 1 0 14 14" fill="none" stroke="#fff" stroke-width="3"/></svg></div>
</section>

<section class="box extinguisher-op">
  <h2 class="box-head">FIRE EXTINGUISHER OPERATION</h2>
  <ul>
    <li>Stand well back from fire (3 M)</li>
    <li>Always face the fire with your back to a clear doorway</li>
    <li>Always be in pairs.</li>
    <li>Use the PASS method</li>
    <li class="pass">P - pull the pin</li>
    <li class="pass">A - aim at edge of fire</li>
    <li class="pass">S - squeeze the handle</li>
    <li class="pass">S - sweep the fire</li>
  </ul>
  <p class="closing">As the fire diminishes, slowly move closer towards the FIRE staying 1 m</p>
</section>

<section class="box equipment">
  <h2 class="box-head">FIRE FIGHTING EQUIPMENT</h2>
  <p style="margin-top:10px">Installed in this building are:</p>
  <p class="kind">Dry Powder Extinguishers (red with white band)</p>
  <p style="margin-top:14px">Check the Extinguisher label for instructions. <svg width="12" height="22" style="vertical-align:middle"><rect width="12" height="22" rx="4" fill="var(--alert-red)"/><rect y="9" width="12" height="3" fill="#fff"/></svg></p>
  <p style="margin-top:10px;font-size:9px">Under no circumstances should you use water on or near live electrical equipment.</p>
</section>

<section class="box key-table">
  <div class="key-row" style="top:10px"><span class="icon"><svg width="20" height="20"><circle cx="10" cy="10" r="7" fill="#fff" stroke="var(--alert-red)" stroke-width="3"/></svg></span><span class="name">HOSEREEL</span></div>
  <div class="key-row" style="top:36px;height:30px"><span class="icon"><svg width="20" height="26"><rect width="20" height="26" fill="var(--alert-red)"/></svg></span><span class="name">FIRE INDICATOR PANEL</span></div>
  <div class="key-row" style="top:72px"><span class="icon"><svg width="20" height="20"><rect width="20" height="20" fill="var(--alert-red)"/><rect x="6" y="6" width="8" height="8" fill="#fff"/></svg></span><span class="name">MANUAL CALL POINT</span></div>
  <div class="key-row" style="top:96px"><span class="icon"><svg width="12" height="20"><rect width="12" height="20" rx="4" fill="var(--alert-red)"/></svg></span><span class="name">EXTINGUISHER</span></div>
  <div class="key-row" style="top:122px"><span class="icon"><svg width="26" height="18"><rect width="26" height="18" fill="var(--alert-red)"/><text x="13" y="14" font-size="11" font-weight="700" fill="#fff" text-anchor="middle">FB</text></svg></span><span class="name">FIRE BLANKET</span></div>
  <div class="key-row" style="top:142px"><span class="icon"><svg width="20" height="18"><rect width="20" height="18" fill="var(--safe-green)"/><path d="M8 3h4v4h4v4h-4v4H8v-4H4V7h4z" fill="#fff"/></svg></span><span class="name">FIRST AID</span></div>
  <div class="key-row" style="top:162px"><span class="icon"><svg width="24" height="18"><rect width="24" height="18" fill="#111"/><polygon points="14,1 6,10 12,10 9,17 18,7 12,7" fill="#f5c400"/></svg></span><span class="name">SWITCH BOARD</span></div>
  <div class="key-row" style="top:182px"><span class="icon"><svg width="26" height="18"><rect width="26" height="18" fill="var(--safe-green)"/><text x="13" y="13" font-size="9" font-weight="700" fill="#fff" text-anchor="middle">EXIT</text></svg></span><span class="name">EXIT SIGN</span></div>
  <div class="key-row" style="top:202px"><span class="icon"><svg width="26" height="16"><polygon points="0,5 14,5 14,0 26,8 14,16 14,11 0,11" fill="#fff" stroke="var(--safe-green)" stroke-width="2"/></svg></span><span class="name">PATH OF EXIT</span></div>
  <div class="key-row" style="top:222px"><span class="icon"><svg width="26" height="6"><rect width="26" height="4" fill="var(--safe-green)"/></svg></span><span class="name">MAIN PATH</span></div>
  <div class="key-row" style="top:242px"><span class="icon"><svg width="26" height="6"><g fill="var(--safe-green)"><rect width="4" height="4"/><rect x="7" width="4" height="4"/><rect x="14" width="4" height="4"/><rect x="21" width="4" height="4"/></g></svg></span><span class="name">ALTERNATE PATH</span></div>
  <div class="key-row" style="top:264px"><span class="icon"><svg width="26" height="18"><rect width="26" height="18" fill="var(--safe-green)"/><text x="13" y="12" font-size="6" fill="#fff" text-anchor="middle">AA</text></svg></span><span class="name">ASSEMBLY AREA</span></div>
</section>

<section class="box race">
  <div class="race-inner">
    <p class="big">IN CASE OF FIRE</p>
    <p class="small">FIRE/ EVACUATION PROCEDURES</p>
  </div>
  <p class="race-step" style="top:92px"><b>R</b>EMOVE PEOPLE</p>
  <p class="race-note" style="top:124px">IF IN DANGER TO THE <em>ASSEMBLY POINT</em></p>
  <p class="race-step" style="top:142px"><b>A</b>LERT THE FIRE SERVICE</p>
  <p class="race-note" style="top:174px">NEARBY RESIDENCE AND MEMBERS OF THE PUBLIC</p>
  <p class="race-step" style="top:192px"><b>C</b>ONFINE FIRE &amp; SMOKE</p>
  <p class="race-note" style="top:224px">CLOSE ALL WINDOWS &amp; DOORS (IF SAFE TO DO SO)</p>
  <p class="race-step" style="top:242px"><b>E</b>XTINGUISH</p>
  <p class="race-note" style="top:274px">AND CONTROL THE FIRE (IF SAFE TO DO SO)</p>
</section>
</body>
</html>
```